Stonefield Partners Business Card Design

We are looking for a new business card design, we are not happy with our current design. We are a boutique management consulting firm and our clients are typically fortune 500 companies.

I have attached the current front and back that we have as well as a version of our logo that can be used. I am trying to get a higher resolution version of the logo file to upload to the project.

Target Market(s)

Fortune 500 companies are our primary client base. Financial services, life sciences, pharmaceuticals and telecom companies are

Industry/Entity Type

Management Consulting

Contact Information for Business Card

We are trying to communicate a high degree of professionalism, a somewhat minimalist perhaps with some air of whimsy (without overdoing it). Attached is the current design, front and back as well as logos. I like the current back of the card and assume we will keep the phrase the same.

From a color palette perspective, I prefer to stay with a gray scale as they are today.

Font styles to use
Sans Serif

Colors
1b1b1b
474747
ffffff

Requirements
Must have
• Two sided business card design. File format should be something that can be used outside of Photoshop like MS Publisher so that they can be edited with personal information.
• Font should be calibri or something very similar and should be available within MS Office
Should not have
• No other logos or graphics outside of the logo provided.

```html
<!DOCTYPE html>
<html lang="en">
<head>
<meta charset="utf-8">
<title>Stonefield Partners Business Card</title>
<link rel="stylesheet" href="https://fonts.googleapis.com/css2?family=Open+Sans:wght@400;600;700&display=swap">
<style>
  :root {
    --ink: #1b1b1b;
    --mid: #474747;
    --paper: #ffffff;
    --card-dark: #2a2a2a;
    --backdrop: #e6e4e1;
  }
  * { margin: 0; padding: 0; box-sizing: border-box; }
  html, body { width: 1200px; height: 1000px; overflow: hidden; }
  body {
    background: var(--backdrop);
    font-family: "Open Sans", Arial, sans-serif;
    position: relative;
  }
  .card {
    position: absolute;
    left: 265px;
    width: 666px;
    height: 397px;
    border-radius: 24px;
  }
  .card-front { top: 73px; background: var(--paper); color: var(--ink); }
  .card-back { top: 532px; background: var(--card-dark); color: var(--paper); }

  .wordmark {
    position: absolute;
    font-weight: 700;
    letter-spacing: -0.5px;
    line-height: 1;
    display: flex;
    align-items: center;
  }
  .wordmark .dot {
    display: inline-block;
    border-radius: 50%;
    margin-right: 12px;
  }
  .card-front .wordmark { left: 32px; top: 44px; font-size: 48px; color: var(--ink); }
  .card-front .wordmark .dot { width: 22px; height: 22px; background: var(--ink); }
  .card-back .wordmark {
    left: 0; right: 0; top: 160px;
    justify-content: center;
    font-size: 72px;
    color: var(--paper);
  }
  .card-back .wordmark .dot { width: 30px; height: 30px; background: var(--paper); }

  .contact {
    position: absolute;
    left: 374px;
    top: 140px;
    color: var(--ink);
  }
  .contact .person-name { font-size: 20px; font-weight: 700; line-height: 24px; letter-spacing: 0.3px; }
  .contact .person-title { font-size: 15.5px; line-height: 20px; color: var(--mid); }
  .contact .company { margin-top: 25px; font-size: 15.5px; font-weight: 700; line-height: 22px; }
  .contact .address { font-size: 15.5px; line-height: 20px; font-style: normal; }
  .contact .channels { margin-top: 8px; list-style: none; font-size: 15px; line-height: 23px; }
  .contact .channels li { display: flex; align-items: center; }
  .contact .channels svg { width: 14px; height: 14px; margin-right: 8px; fill: var(--ink); flex: none; }
  .contact .channels b { font-weight: 700; }

  .tagline {
    position: absolute;
    left: 0; right: 0; top: 347px;
    text-align: center;
    font-size: 16px;
    color: var(--paper);
  }
</style>
</head>
<body>
  <section class="card card-front">
    <div class="wordmark"><span class="dot"></span>Stonefield</div>
    <div class="contact">
      <p class="person-name">DANA WHITFIELD</p>
      <p class="person-title">Managing Director</p>
      <p class="company">Stonefield Partners, Inc.</p>
      <address class="address">218 Harlow Crescent<br>Suite 410<br>Cedar Point, WA 98021</address>
      <ul class="channels">
        <li>
          <svg viewBox="0 0 16 16" aria-hidden="true"><path d="M3 2h3l1.5 3.5-2 1.3a8 8 0 0 0 3.7 3.7l1.3-2L14 10v3a1 1 0 0 1-1 1A12 12 0 0 1 2 3a1 1 0 0 1 1-1z"/></svg>
          555.214.3870
        </li>
        <li>
          <svg viewBox="0 0 16 16" aria-hidden="true"><path d="M1 3h14v10H1z M2.2 4l5.8 4.5L13.8 4z" fill-rule="evenodd"/></svg>
          dwhitfield@stonefieldpartners.com
        </li>
        <li>
          <svg viewBox="0 0 16 16" aria-hidden="true"><path d="M8 1a7 7 0 1 0 0 14A7 7 0 0 0 8 1zm0 1.5c.9 0 1.9 1.7 2.2 4.5H5.8C6.1 4.2 7.1 2.5 8 2.5zM2.6 7h1.9c.1-1.6.4-3 1-3.9A5.5 5.5 0 0 0 2.6 7zm8.9 0h1.9a5.5 5.5 0 0 0-2.9-3.9c.6.9.9 2.3 1 3.9zM2.6 9a5.5 5.5 0 0 0 2.9 3.9c-.6-.9-.9-2.300-1-3.9zm3.2 0c.3 2.8 1.3 4.5 2.2 4.5s1.9-1.7 2.2-4.5zm5.7 0c-.1 1.6-.4 3-1 3.9A5.5 5.5 0 0 0 13.4 9z"/></svg>
          <span>www.<b>stonefieldpartners</b>.com</span>
        </li>
      </ul>
    </div>
  </section>

  <section class="card card-back">
    <div class="wordmark"><span class="dot"></span>Stonefield</div>
    <p class="tagline">Clear thinking for the work that matters most</p>
  </section>
</body>
</html>
```